Supplement Company Needs a Protein Powder Pouch Design

We are looking for a modern and fresh design for our 500g pouches of protein powder as our current design is not eye catching or exciting enough.

This new design will be printed on both sides of a 178mm x 280mm x 101mm pouch.

We have 4 flavours. These are Banana Ice Cream, Chocolate Deluxe, Strawberries & Cream and Vanilla Ice Cream.

Industry/Entity Type

Supplement

Requirements
Must have
• Attractive and eye catching front and space for all the nutritional information and ingredients on the back.

Must clearly state 'food supplement' somewhere on the front of the pouch.
Nice to have
• Our logo is attached.
Should not have
• No health claims as these are not allowed in the UK

```html
<!DOCTYPE html>
<html lang="en">
<head>
<meta charset="utf-8">
<title>Protein Powder Pouch Range</title>
<link rel="stylesheet" href="https://fonts.googleapis.com/css2?family=Montserrat:wght@700;800;900&family=Lobster&family=Open+Sans:wght@400;700&display=swap">
<style>
  :root {
    --page: #ffffff;
    --ink: #1d1d1b;
    --leaf: #6cae2e;
    --choc-cream: #f6e7cc;
    --choc-peach: #f4b25a;
    --choc-dark: #4a1d12;
    --choc-accent: #e0137f;
    --choc-script: #f3a63b;
    --nana-cream: #f4f1cf;
    --nana-yellow: #f5d02f;
    --nana-deep: #e9b51c;
    --nana-green: #0f6a39;
  }
  * { box-sizing: border-box; margin: 0; padding: 0; }
  html, body { width: 1200px; height: 493px; overflow: hidden; background: var(--page); }
  body { position: relative; font-family: "Open Sans", Arial, sans-serif; color: var(--ink); }

  .pouch {
    position: absolute; top: 38px; width: 270px; height: 417px;
    border-radius: 10px 10px 14px 14px; overflow: hidden;
  }
  .pouch--choc-front { left: 30px; }
  .pouch--choc-back { left: 320px; }
  .pouch--nana-front { left: 610px; }
  .pouch--nana-back { left: 900px; }

  .pouch--choc { background: linear-gradient(180deg, var(--choc-cream) 0%, #f7dcb0 55%, var(--choc-peach) 100%); }
  .pouch--nana { background: linear-gradient(180deg, var(--nana-cream) 0%, #f3e99a 55%, var(--nana-yellow) 100%); }

  .brand {
    position: absolute; left: 0; right: 0; display: flex; justify-content: center; align-items: center; gap: 4px;
    font-family: "Montserrat", Arial, sans-serif; font-weight: 800; font-size: 24px; color: var(--ink); letter-spacing: -0.5px;
  }
  .brand__dot { width: 7px; height: 7px; border-radius: 50%; background: var(--leaf); }
  .pouch .brand--top { top: 82px; }
  .pouch .brand--bottom { top: 330px; }

  .tag {
    position: absolute; top: 121px; left: 50%; transform: translateX(-50%);
    padding: 2px 11px; border-radius: 10px; color: #fff;
    font-family: "Montserrat", Arial, sans-serif; font-weight: 800; font-size: 9.5px; letter-spacing: 0.3px; white-space: nowrap;
  }
  .pouch--choc .tag { background: var(--choc-accent); }
  .pouch--nana .tag { background: var(--nana-green); }

  .headline {
    position: absolute; left: 0; right: 0; top: 142px; height: 66px;
    font-family: "Montserrat", Arial, sans-serif; font-weight: 900; font-size: 32px; line-height: 32px; letter-spacing: -0.6px;
    white-space: nowrap;
  }
  .headline span { display: block; }
  .headline__one { padding-left: 44px; }
  .headline__two { padding-left: 64px; }
  .headline::before, .headline::after { content: ""; position: absolute; height: 22px; }
  .headline::before { left: 0; width: 56px; top: 38px; }
  .headline::after { left: 226px; right: 0; top: 6px; }
  .pouch--choc .headline { color: var(--choc-accent); }
  .pouch--choc .headline::before, .pouch--choc .headline::after { background: var(--choc-accent); }
  .pouch--nana .headline { color: var(--nana-green); }
  .pouch--nana .headline::before, .pouch--nana .headline::after { background: var(--nana-green); }

  .art { position: absolute; left: 0; right: 0; top: 230px; bottom: 0; }
  .art--choc { background: radial-gradient(ellipse at 50% 30%, #8a4a2c 0%, #5b2617 55%, var(--choc-dark) 100%); clip-path: ellipse(85% 78% at 50% 100%); }
  .art--nana { background: radial-gradient(ellipse at 50% 35%, #f7dc57 0%, var(--nana-yellow) 50%, var(--nana-deep) 100%); clip-path: ellipse(85% 80% at 50% 100%); }

  .flavour {
    position: absolute; left: 0; right: 0; top: 352px; text-align: center;
    font-family: "Lobster", cursive; font-size: 27px;
  }
  .pouch--choc-front .flavour { color: var(--choc-script); }
  .pouch--nana-front .flavour { color: var(--ink); }
  .weight {
    position: absolute; left: 0; right: 0; top: 388px; text-align: center;
    font-family: "Montserrat", Arial, sans-serif; font-weight: 800; font-size: 9px;
  }
  .pouch--choc-front .weight { color: #fff; }

  .back-title { position: absolute; left: 0; right: 0; top: 66px; text-align: center; }
  .back-title__script { font-family: "Lobster", cursive; font-size: 16px; display: block; }
  .back-title__main { font-family: "Montserrat", Arial, sans-serif; font-weight: 900; font-size: 22px; display: block; line-height: 1.05; }
  .back-title__sub { font-family: "Montserrat", Arial, sans-serif; font-weight: 800; font-size: 9.5px; display: block; }
  .pouch--choc-back .back-title { color: var(--choc-dark); }
  .pouch--nana-back .back-title { color: var(--nana-green); }

  .label-copy { position: absolute; left: 22px; right: 22px; top: 140px; font-size: 4.6px; line-height: 1.35; color: var(--ink); }
  .label-copy p { margin-bottom: 4px; }
  .label-copy strong { font-weight: 700; }

  .nutrition { position: absolute; left: 22px; top: 283px; border-collapse: collapse; width: 226px; font-size: 3.8px; background: #fff; }
  .nutrition td, .nutrition th { border: 0.4px solid var(--ink); padding: 1px 2px; text-align: left; font-weight: 400; }
  .nutrition th { font-weight: 700; }
  .nutrition .kcal { font-weight: 700; font-size: 6px; text-align: center; }

  .address { position: absolute; left: 0; right: 0; top: 368px; text-align: center; font-size: 4.8px; font-weight: 700; color: var(--ink); }
</style>
</head>
<body>

  <section class="pouch pouch--choc pouch--choc-front">
    <div class="brand brand--top"><span class="brand__dot"></span>BRISK</div>
    <div class="tag">FOOD SUPPLEMENT</div>
    <div class="art art--choc" role="img" aria-label="Chocolate pieces splashing into flowing melted chocolate"></div>
    <h1 class="headline"><span class="headline__one">PROTEIN</span><span class="headline__two">POWDER</span></h1>
    <div class="flavour">Chocolate Deluxe</div>
    <div class="weight">500g</div>
  </section>

  <section class="pouch pouch--choc pouch--choc-back">
    <div class="back-title">
      <span class="back-title__script">Chocolate Deluxe</span>
      <span class="back-title__main">PROTEIN POWDER</span>
      <span class="back-title__sub">FOOD SUPPLEMENT</span>
    </div>
    <div class="label-copy">
      <p><strong>INGREDIENTS:</strong><br>Protein Blend (Soya Protein Isolate, Whey Protein Concentrate (<strong>Milk</strong>), <strong>Milk</strong> Protein) (70%), Acetyl L-Carnitine (500mg per 100g), Acai Berry 4:1 Extract (400mg per 100g), Green Tea Extract (400mg per 100g), Conjugated Linoleic Acid Powder (50mg per 100g), Flavouring, Fat Reduced Cocoa Powder (10%), Thickener (Xanthan Gum), Sweetener (Sucralose).</p>
      <p>Manufactured in the UK with EU protein powder (Germany) and non-EU cocoa powder (Ghana).</p>
      <p><strong>ALLERGEN INFORMATION:</strong><br>For allergens, see ingredients in bold. May also contain cereal containing gluten, nuts, egg, peanuts.</p>
      <p><strong>CAUTION:</strong><br>Food supplements should not be used as a substitute for a varied diet and healthy lifestyle. This product is not recommended for use by pregnant or lactating women. If you are taking any medications or are under medical supervision, you should consult with your health care professional before use, taking into consideration other supplements and medications you consume. This product is not intended for use by persons under the age of 18.</p>
    </div>
    <table class="nutrition">
      <tr><th>Nutrition</th><th>Per 30g</th><th>Per 100g</th><th>Per 30g</th><th>Per 100g</th><td class="kcal" rowspan="4">Calories<br>117</td></tr>
      <tr><td>Energy</td><td>485kJ</td><td>1617kJ</td><td>Carbs 4.2g</td><td>14g</td></tr>
      <tr><td>Fat</td><td>1.8g</td><td>6g</td><td>Protein 21g</td><td>70g</td></tr>
      <tr><td>Salt</td><td>0.2g</td><td>0.6g</td><td>Sugars 3g</td><td>10g</td></tr>
    </table>
    <div class="brand brand--bottom"><span class="brand__dot"></span>BRISK</div>
    <div class="address">Brisk Supplements Limited, Mill Lane, Eastbury, Somerset, TA9 2QP.</div>
  </section>

  <section class="pouch pouch--nana pouch--nana-front">
    <div class="brand brand--top"><span class="brand__dot"></span>BRISK</div>
    <div class="tag">FOOD SUPPLEMENT</div>
    <div class="art art--nana" role="img" aria-label="Bunch of bananas with a banana slice in a splash of yellow milkshake"></div>
    <h1 class="headline"><span class="headline__one">PROTEIN</span><span class="headline__two">POWDER</span></h1>
    <div class="flavour">Banana Ice Cream</div>
    <div class="weight">500g</div>
  </section>

  <section class="pouch pouch--nana pouch--nana-back">
    <div class="back-title">
      <span class="back-title__script">Chocolate Deluxe</span>
      <span class="back-title__main">PROTEIN POWDER</span>
      <span class="back-title__sub">FOOD SUPPLEMENT</span>
    </div>
    <div class="label-copy">
      <p><strong>INGREDIENTS:</strong><br>Protein Blend (Soya Protein Isolate, Whey Protein Concentrate (<strong>Milk</strong>), <strong>Milk</strong> Protein) (70%), Acetyl L-Carnitine (500mg per 100g), Acai Berry 4:1 Extract (400mg per 100g), Green Tea Extract (400mg per 100g), Conjugated Linoleic Acid Powder (50mg per 100g), Flavouring, Fat Reduced Cocoa Powder (10%), Thickener (Xanthan Gum), Sweetener (Sucralose).</p>
      <p>Manufactured in the UK with EU protein powder (Germany) and non-EU cocoa powder (Ghana).</p>
      <p><strong>ALLERGEN INFORMATION:</strong><br>For allergens, see ingredients in bold. May also contain cereal containing gluten, nuts, egg, peanuts.</p>
      <p><strong>CAUTION:</strong><br>Food supplements should not be used as a substitute for a varied diet and healthy lifestyle. This product is not recommended for use by pregnant or lactating women. If you are taking any medications or are under medical supervision, you should consult with your health care professional before use, taking into consideration other supplements and medications you consume. This product is not intended for use by persons under the age of 18.</p>
    </div>
    <table class="nutrition">
      <tr><th>Nutrition</th><th>Per 30g</th><th>Per 100g</th><th>Per 30g</th><th>Per 100g</th><td class="kcal" rowspan="4">Calories<br>117</td></tr>
      <tr><td>Energy</td><td>485kJ</td><td>1617kJ</td><td>Carbs 4.2g</td><td>14g</td></tr>
      <tr><td>Fat</td><td>1.8g</td><td>6g</td><td>Protein 21g</td><td>70g</td></tr>
      <tr><td>Salt</td><td>0.2g</td><td>0.6g</td><td>Sugars 3g</td><td>10g</td></tr>
    </table>
    <div class="brand brand--bottom"><span class="brand__dot"></span>BRISK</div>
    <div class="address">Brisk Supplements Limited, Mill Lane, Eastbury, Somerset, TA9 2QP.</div>
  </section>

</body>
</html>
```